New Business Card Design Project

Hi! I would like for you to design a business card for our aesthetic injections business. We offer Velmo, filler, skin care. I would like it to be elegant, feminine, modern and sleek/clean. I like black/gold foil/ivory/parchment colors. It can be either one or two sided. I would like matte black with gold foil logo on one side and ivory with gold foil information on the other side

Target Market(s)

target market is the discerning woman who wants to look her best

Industry/Entity Type

beauty

Contact Information for Business Card

logo, name, phone, email, website, instagram, facebook, location

Requirements
Must have
• logo and info
Nice to have
• the icons for cell, instagram, email, fb etc
Should not have
• images of people

```html
<!DOCTYPE html>
<html lang="en">
<head>
<meta charset="utf-8">
<title>The Ivoria Lounge — Business Card</title>
<link rel="stylesheet" href="https://fonts.googleapis.com/css2?family=Open+Sans:wght@400;600;700&display=swap">
<style>
  :root {
    --backdrop: #3a3a3a;
    --card-black: #111112;
    --gold: #c8b27a;
    --gold-soft: #a8955f;
    --gold-edge: #d4c48a;
  }
  * { margin: 0; padding: 0; box-sizing: border-box; }
  html, body {
    width: 1200px; height: 801px; overflow: hidden;
    background: var(--backdrop);
    font-family: "Open Sans", Arial, sans-serif;
  }
  .stage {
    position: relative; width: 1200px; height: 801px;
    display: flex; align-items: center; justify-content: center; gap: 40px;
  }
  .card {
    position: relative; width: 530px; height: 303px;
    background: var(--card-black);
    border: 1.5px solid var(--gold-edge);
    border-radius: 3px;
  }
  /* Front: contact side */
  .card-info .person {
    position: absolute; right: 300px; top: 150px; text-align: right;
  }
  .person-name {
    color: var(--gold); font-weight: 700; font-size: 19px; letter-spacing: 0.5px;
    white-space: nowrap;
  }
  .person-title {
    color: var(--gold-soft); font-size: 12px; margin-top: 2px;
  }
  .divider {
    position: absolute; left: 250px; top: 100px; width: 1.5px; height: 104px;
    background: var(--gold-soft);
  }
  .contact-list {
    position: absolute; left: 268px; top: 100px; list-style: none;
  }
  .contact-list li {
    display: flex; align-items: center; gap: 7px;
    color: var(--gold); font-size: 12px; line-height: 21px; white-space: nowrap;
  }
  .contact-list svg { width: 11px; height: 11px; flex: none; }
  /* Back: brand side */
  .card-brand { display: flex; align-items: center; justify-content: center; }
  .brand-mark {
    width: 200px; height: 200px; border: 1.5px solid var(--gold);
    border-radius: 50%;
    display: flex; align-items: center; justify-content: center;
  }
  .brand-name {
    color: var(--gold); font-weight: 400; font-size: 20px; letter-spacing: 1px;
    text-align: center; line-height: 1.3;
  }
</style>
</head>
<body>
<main class="stage">
  <section class="card card-info" aria-label="Contact side">
    <div class="person">
      <p class="person-name">DARIN KOVAL</p>
      <p class="person-title">President</p>
    </div>
    <div class="divider"></div>
    <ul class="contact-list">
      <li>
        <svg viewBox="0 0 12 12" aria-hidden="true"><path d="M3 1l2 2.5-1.2 1.2a6 6 0 0 0 3.5 3.5L8.5 7 11 9l-1.2 2A9 9 0 0 1 1 2.2Z" fill="var(--gold)"/></svg>
        555.204.6138
      </li>
      <li>
        <svg viewBox="0 0 12 12" aria-hidden="true"><rect x="1" y="2.5" width="10" height="7" rx="1" fill="var(--gold)"/><path d="M1.5 3l4.5 3.5L10.5 3" stroke="var(--card-black)" fill="none"/></svg>
        dkoval@TheIvoriaLounge.com
      </li>
      <li>
        <svg viewBox="0 0 12 12" aria-hidden="true"><circle cx="6" cy="6" r="5" fill="none" stroke="var(--gold)" stroke-width="1.2"/><path d="M1 6h10M6 1c-2 3-2 7 0 10M6 1c2 3 2 7 0 10" stroke="var(--gold)" fill="none" stroke-width="0.9"/></svg>
        www.TheIvoriaLounge.com
      </li>
      <li>
        <svg viewBox="0 0 12 12" aria-hidden="true"><circle cx="6" cy="6" r="5" fill="var(--gold)"/></svg>
        @The_Ivoria_Lounge
      </li>
      <li>
        <svg viewBox="0 0 12 12" aria-hidden="true"><rect x="1" y="1" width="10" height="10" fill="var(--gold)"/></svg>
        @The_Ivoria_Lounge
      </li>
    </ul>
  </section>

  <section class="card card-brand" aria-label="Brand side">
    <div class="brand-mark">
      <p class="brand-name">The Ivoria<br>Lounge</p>
    </div>
  </section>
</main>
</body>
</html>
```